Business Card Design for Kidvale (Hires out childrens play areas)

Looking to have a business card designed for a company we just bought. The company rents out childrens play areas.

I have uploaded a couple of examples of the kind of business card style I like. Here are two more examples:

https://quorvastudio.nz/project/bright-romp-branding/
https://imgvaultcdn.com/design_img/8841052/302917/302917_5518203_8841052_b73e19a2_image.jpg

I think a white card will be best due to all the colours in the logo.

Size we require: 3.75" x 2.25" (horizontally orientated) with a 0.125" bleed

Uploaded is two versions of our logo.

Details for the card:
1. My name: Liam Verster
2. Title: Managing Director
3. Phone no: 021 563 417
4. Email: liam@kidvale.co.nz
5. URL: www.kidvale.co.nz
6. Address:
PO Box 318625
Fernlea, Auckland

Let me know if you need anything else.

Target Market(s)

Hospitals, doctors surgeries, bed shops, etc.

Contact Information for Business Card

Details for the card:
1. My name: Liam Verster
3. Phone no: 021 563 417
5. URL: www.kidvale.co.nz
6. Address:
PO Box 318625
Fernlea, Auckland

Requirements
Should not have
• Not too busy.

```html
<!DOCTYPE html>
<html lang="en">
<head>
<meta charset="utf-8">
<title>Kidvale Business Card</title>
<link rel="stylesheet" href="https://fonts.googleapis.com/css2?family=Quicksand:wght@500;600;700&display=swap">
<style>
  :root {
    --stage: #9e268b;
    --card: #ffffff;
    --ink: #3a3a3a;
    --brand-purple: #8e2a8f;
    --brand-blue: #1d5fb6;
    --brand-red: #e2231a;
    --brand-orange: #f28a1e;
    --icon-purple: #8a2a8c;
    --art-pink: #d41c8e;
    --art-violet: #6f2a8f;
  }
  * { box-sizing: border-box; margin: 0; padding: 0; }
  html, body { width: 1200px; height: 1200px; overflow: hidden; }
  body {
    background: var(--stage);
    font-family: "Quicksand", sans-serif;
    position: relative;
  }
  .card {
    position: absolute;
    left: 211px;
    width: 778px;
    height: 444px;
    background: var(--card);
    overflow: hidden;
    box-shadow: 0 14px 30px rgba(60, 0, 50, 0.35);
  }
  .card--front { top: 138px; }
  .card--back { top: 638px; }

  .front-art {
    position: absolute;
    inset: 0;
    background:
      linear-gradient(90deg, rgba(255,214,120,0.75), rgba(255,255,255,0) 20%, rgba(255,255,255,0) 80%, rgba(255,200,60,0.75)),
      linear-gradient(115deg, #b25fae 0%, #f1e79a 18%, #5c63b8 32%, #a8d9c8 46%, #7ccde0 54%, #6cbf4a 66%, #a4a6d8 78%, #e8ea3a 90%, #d39fcc 100%);
  }
  .front-brand {
    position: absolute;
    left: 50%;
    top: 118px;
    transform: translateX(-50%);
    padding: 30px 52px;
    background: var(--card);
    border-radius: 40px;
    font-weight: 700;
    font-size: 76px;
    line-height: 1;
    color: var(--brand-blue);
  }
  .front-url {
    position: absolute;
    left: 253px;
    top: 325px;
    width: 272px;
    height: 37px;
    border-radius: 19px;
    background: var(--card);
    color: var(--brand-purple);
    font-weight: 700;
    font-size: 21px;
    line-height: 37px;
    text-align: center;
  }

  .back-brand {
    position: absolute;
    left: 40px;
    top: 38px;
    font-weight: 700;
    font-size: 46px;
    line-height: 1;
    color: var(--brand-blue);
  }
  .holder {
    position: absolute;
    left: 40px;
    top: 176px;
  }
  .holder__name {
    font-weight: 700;
    font-size: 29px;
    line-height: 1;
  }
  .holder__first { color: var(--brand-blue); }
  .holder__last { color: var(--brand-red); }
  .holder__title {
    margin-top: 2px;
    font-weight: 500;
    font-size: 15px;
    color: var(--brand-orange);
    letter-spacing: 0.3px;
  }
  .contacts {
    position: absolute;
    left: 34px;
    top: 252px;
    list-style: none;
    color: var(--ink);
    font-weight: 500;
    font-size: 20px;
  }
  .contacts li {
    display: flex;
    align-items: center;
    height: 37px;
  }
  .contacts li.contacts__address { height: 54px; line-height: 1.25; }
  .contacts .icon {
    width: 24px;
    flex: 0 0 24px;
    margin-right: 15px;
    color: var(--icon-purple);
    display: flex;
    justify-content: center;
  }
  .contacts .icon--at { font-weight: 700; font-size: 22px; }
  .contacts .phone-num { margin-left: 6px; }

  .back-art {
    position: absolute;
    left: 413px;
    top: 74px;
    width: 460px;
    height: 460px;
    border-radius: 50%;
    background: linear-gradient(170deg, var(--art-violet) 0%, #9a2890 45%, var(--art-pink) 100%);
  }
</style>
</head>
<body>
  <section class="card card--front">
    <div class="front-art" role="img" aria-label="Radiating rainbow stripes illustration"></div>
    <div class="front-brand">Kidvale</div>
    <div class="front-url">www.kidvale.co.nz</div>
  </section>

  <section class="card card--back">
    <div class="back-brand">Kidvale</div>

    <div class="holder">
      <p class="holder__name"><span class="holder__first">Liam</span> <span class="holder__last">Verster</span></p>
      <p class="holder__title">Managing Director</p>
    </div>

    <ul class="contacts">
      <li>
        <span class="icon">
          <svg width="22" height="22" viewBox="0 0 24 24" fill="currentColor"><path d="M6.6 10.8c1.4 2.8 3.8 5.1 6.6 6.6l2.2-2.2c.3-.3.7-.4 1-.2 1.1.4 2.3.6 3.6.6.6 0 1 .4 1 1V20c0 .6-.4 1-1 1C10.6 21 3 13.4 3 4c0-.6.4-1 1-1h3.5c.6 0 1 .4 1 1 0 1.3.2 2.5.6 3.6.1.3 0 .7-.2 1l-2.3 2.2z"/></svg>
        </span>
        <span class="phone-num">021 563 417</span>
      </li>
      <li>
        <span class="icon icon--at">@</span>
        <span>liam@kidvale.co.nz</span>
      </li>
      <li>
        <span class="icon">
          <svg width="22" height="22" viewBox="0 0 24 24" fill="none" stroke="currentColor" stroke-width="2.2" stroke-linecap="round"><path d="M10 14a4 4 0 0 0 5.7 0l3.5-3.5a4 4 0 0 0-5.7-5.7l-1 1"/><path d="M14 10a4 4 0 0 0-5.7 0l-3.5 3.5a4 4 0 0 0 5.7 5.7l1-1"/></svg>
        </span>
        <span>www.kidvale.co.nz</span>
      </li>
      <li class="contacts__address">
        <span class="icon">
          <svg width="22" height="22" viewBox="0 0 24 24" fill="currentColor"><path d="M12 3 2 12h3v9h5v-6h4v6h5v-9h3z"/></svg>
        </span>
        <span>PO Box 318625<br>Fernlea, Auckland</span>
      </li>
    </ul>

    <div class="back-art" role="img" aria-label="Large mascot illustration in purple and pink"></div>
  </section>
</body>
</html>
```